Wine and retail website for a high-end resort community

We are introducing a line of quality wines in the resort community of Saltmere Island, Massachusetts, USA. The site will detail information about the wine, and online store connected to and external government approved shipper for wine, and additional non-alcoholic retail merchandise sales.

We are planning the site to be driven off the Squarespace platform so I do not believe coding is necessary initially; however, the ability to do sop would be helpful if needed.

Attached are the images/files we have available so far. Please feel free to use stock images in your design.

Target Market(s)

Wine enthusiasts in the resort community of Martha’s Vineyard Massachusetts

Industry/Entity Type

Wine

Number of Pages Required

4 page

Font styles to use
Sans Serif

Requirements
Must have
• Home page, about page, wine page, e-commerce page, retail merchandise page. I recently came across brelmorcellars.com and really like the look and layout of their pages if that helps
Nice to have
• A short wine/Martha’s Vineyard related video on the home page

```html
<!DOCTYPE html>
<html lang="en">
<head>
<meta charset="utf-8">
<title>Saltmere Estates — Website Presentation</title>
<link rel="stylesheet" href="https://fonts.googleapis.com/css2?family=Poppins:wght@300;400;500;600;700;800&display=swap">
<style>
:root{
  --ink:#141414;
  --dark:#161616;
  --dark-2:#1f1f1f;
  --muted:#6d6d6d;
  --line:#e4e4e4;
  --soft:#f7f7f9;
  --lav:#c9c3f2;
  --gold:#f0a21a;
  --red:#d8333b;
  --white:#ffffff;
}
*{box-sizing:border-box;margin:0;padding:0}
html,body{width:1200px;height:3125px;overflow:hidden}
body{font-family:"Poppins",sans-serif;color:var(--ink);background:var(--white);position:relative}
.board-bg{position:absolute;inset:0;background:
  linear-gradient(180deg,#ece9fb 0%,#f7f6fd 8%,#fbfbf7 18%,#f6f7ef 30%,#ffffff 40%,#ffffff 100%);}
.board-scene{position:absolute;left:0;top:120px;width:1200px;height:930px;
  background:linear-gradient(180deg,rgba(240,238,232,.0) 0%,rgba(232,234,220,.55) 45%,rgba(226,232,212,.45) 70%,rgba(255,255,255,0) 100%);}
.brand-top{position:absolute;top:60px;left:0;width:1200px;text-align:center}
.brand-top .name{font-size:44px;font-weight:600;letter-spacing:1px;line-height:1.05;color:#2a2a2a}
.brand-top .sub{font-size:14px;font-weight:500;letter-spacing:10px;color:#2a2a2a;margin-top:10px}
.brand-top .dot{display:inline-block;width:14px;height:14px;border-radius:50%;background:#9a9a9a;margin-bottom:12px}

.site{position:absolute;left:274px;top:244px;width:655px;box-shadow:0 10px 40px rgba(0,0,0,.08)}
.sec{position:relative;width:655px;overflow:hidden}
.inner{position:absolute;left:94px;width:466px}
.h2{font-size:13px;font-weight:300;letter-spacing:.2px;text-align:center}
.h2 b{font-weight:800}
.lede{font-size:6px;line-height:1.7;color:var(--muted);text-align:center}

/* hero */
.hero{height:362px}
.hero-photo{position:absolute;inset:0;background:
  linear-gradient(180deg,#b7aff0 0%,#d6d2f2 22%,#bcc6c0 40%,#8ea37a 58%,#6f8a52 75%,#9fb07a 88%,#ffffff 100%)}
.hero-bottles{position:absolute;left:440px;top:80px;width:165px;height:220px;border-radius:8px;
  background:linear-gradient(160deg,rgba(30,20,20,.75),rgba(50,30,30,.55))}
.hero-edge{position:absolute;left:0;bottom:0;width:655px;height:40px}
.nav{position:absolute;top:18px;left:0;width:655px;height:22px}
.nav a{position:absolute;top:7px;font-size:5.5px;color:#333;text-decoration:none}
.nav .logo{position:absolute;left:304px;top:2px;width:50px;text-align:center;font-size:7px;font-weight:600;line-height:1;color:#222}
.nav .icons{position:absolute;right:95px;top:6px;display:flex;gap:10px}
.hero-copy{position:absolute;left:94px;top:118px;width:280px}
.hero-copy h1{font-size:20px;font-weight:300;line-height:1.08;color:#1a1a1a}
.hero-copy h1 b{font-weight:800}
.hero-copy p{font-size:5.5px;line-height:1.7;color:#333;margin-top:7px;width:290px}
.btns{display:flex;gap:10px;margin-top:12px;align-items:center}
.btn-dark{background:#1a1a1a;color:#fff;font-size:5px;padding:4px 8px;border-radius:8px}
.btn-line{font-size:5px;padding:4px 8px;background:rgba(255,255,255,.9);border-radius:8px}

/* about */
.about{height:333px;background:var(--white)}
.about-photo{position:absolute;left:94px;top:49px;width:196px;height:244px;border-radius:98px 98px 0 0;
  background:linear-gradient(160deg,#8aa244 0%,#c4cf6a 40%,#6c7f38 75%,#b75a6a 100%)}
.about-bottle{position:absolute;left:262px;top:95px;width:44px;height:200px;border-radius:14px 14px 4px 4px;
  background:linear-gradient(90deg,#1c1416,#3a2a2c 50%,#1c1416)}
.about-copy{position:absolute;left:343px;top:128px;width:220px}
.about-copy h3{font-size:13px;font-weight:300}
.about-copy h3 b{font-weight:800}
.about-copy p{font-size:5.5px;line-height:1.8;color:#444;margin-top:8px}
.link-line{display:inline-block;margin-top:12px;font-size:5px;padding:3px 8px;border-bottom:1px solid #ccc}

/* offer */
.offer{height:338px;background:var(--dark);color:#fff}
.offer .lede{color:#bcbcbc}
.offer-cards{position:absolute;left:94px;top:100px;display:flex;gap:11px}
.offer-card{width:148px;text-align:center}
.offer-card .ph{height:176px;border-radius:26px}
.offer-card span{display:block;margin-top:12px;font-size:9px;letter-spacing:.3px}

/* winemaking */
.wine-making{height:410px;background:var(--white)}
.video{position:absolute;left:94px;top:100px;width:466px;height:229px;border-radius:10px;
  background:linear-gradient(180deg,#39424a 0%,#5a646b 45%,#2d353b 100%)}
.play{position:absolute;left:219px;top:101px}
.stats{position:absolute;left:94px;top:343px;width:466px;display:grid;grid-template-columns:repeat(4,1fr);text-align:center}
.stats b{display:block;font-size:23px;font-weight:700;line-height:1}
.stats span{font-size:5.5px;color:#555}

/* shortlist */
.shortlist{height:289px;background:var(--soft)}
.products{position:absolute;left:94px;top:101px;display:flex;gap:9px}
.product{width:110px;height:152px;background:#fff;text-align:center;padding-top:12px}
.product .bottle{width:22px;height:60px;margin:0 auto;border-radius:8px 8px 3px 3px;background:linear-gradient(90deg,#1b1416,#3b2b2e 50%,#1b1416)}
.product .shadow{width:80px;height:2px;margin:0 auto;background:linear-gradient(90deg,transparent,#ddd,transparent)}
.stars{color:var(--gold);font-size:6px;letter-spacing:1px;margin-top:10px}
.product h4{font-size:5.5px;font-weight:600;margin-top:6px;line-height:1.4}
.price{font-size:5px;color:#999;margin-top:6px}
.price b{color:var(--gold)}
.arrow{position:absolute;top:171px;width:14px;height:14px;border-radius:4px;display:flex;align-items:center;justify-content:center}

/* news */
.news{height:446px;background:var(--white)}
.news h3{position:absolute;left:94px;top:58px;font-size:13px;font-weight:800}
.news .sub{position:absolute;left:94px;top:78px;width:250px;font-size:5px;line-height:1.5;color:#777}
.view-all{position:absolute;left:482px;top:58px;width:78px;height:18px;border:1px solid var(--red);font-size:4.5px;display:flex;align-items:center;justify-content:space-around}
.big-photo{position:absolute;left:94px;top:105px;width:306px;height:115px;background:linear-gradient(135deg,#4a5a85,#2b2f55 50%,#5e6a42)}
.article{font-size:5px}
.article .meta{color:#999;font-size:4.5px}
.article h5{font-size:5.5px;font-weight:600;line-height:1.5;margin-top:5px}
.article p{color:#888;line-height:1.6;margin-top:6px}
.author{display:flex;align-items:center;gap:5px;margin-top:10px}
.author i{width:18px;height:18px;border-radius:50%;background:#b8a89a;display:block}
.author b{font-size:6px;font-weight:500;display:block}
.author small{font-size:4.5px;color:#999}
.article.feature{position:absolute;left:412px;top:105px;width:148px}
.news-row{position:absolute;left:94px;top:232px;display:flex;gap:11px}
.news-row .article{width:148px}
.news-row .ph{height:88px;margin-bottom:8px}

/* contact */
.contact{height:421px;background:var(--dark);color:#fff}
.contact .h2 b{font-weight:800}
.info{position:absolute;left:133px;top:64px;width:136px;background:var(--dark-2)}
.info div{height:30px;display:flex;align-items:center;gap:8px;padding-left:10px;border-bottom:1px solid #2c2c2c;font-size:6px}
.info small{display:block;font-size:4.5px;color:#999}
.map{position:absolute;left:269px;top:64px;width:254px;height:91px;background:linear-gradient(135deg,#efe6d2,#e3dccb 40%,#d7e2cf)}
.query{position:absolute;left:133px;top:166px;font-size:6.5px;font-weight:700}
.form{position:absolute;left:133px;top:183px;width:390px;height:194px;background:var(--dark-2);padding:14px 24px}
.grid2{display:grid;grid-template-columns:1fr 1fr;gap:12px 14px}
.field{font-size:5px;border-bottom:1px solid #3a3a3a;padding-bottom:6px}
.field span{display:block;color:#888;font-size:4.5px;margin-top:4px}
.field.full{grid-column:1/3;border:none}
.submit{position:absolute;left:171px;top:164px;width:48px;height:16px;background:#fff;color:#111;font-size:5px;display:flex;align-items:center;justify-content:center}

/* footer */
.footer{height:116px;background:var(--dark);color:#fff;border-top:1px solid #2e2e2e}
.f-brand{position:absolute;left:94px;top:20px;width:150px}
.f-brand b{font-size:9px;font-weight:600;display:flex;align-items:center;gap:4px}
.f-brand p{font-size:4.8px;color:#aaa;line-height:1.6;margin-top:8px}
.f-col{position:absolute;top:36px;font-size:4.8px;color:#bbb;line-height:2}
.f-col h6{font-size:6px;color:#fff;font-weight:600;margin-bottom:2px}
.news-form{display:flex;margin-top:4px}
.news-form span{width:76px;height:10px;border:1px solid #444;font-size:3.8px;padding:2px 4px;color:#888}
.news-form em{width:34px;height:10px;background:#fff;color:#111;font-size:3.8px;font-style:normal;display:flex;align-items:center;justify-content:center}
.copy{position:absolute;left:0;bottom:4px;width:655px;text-align:center;font-size:4.5px;color:#999;border-top:1px solid #2e2e2e;padding-top:4px}

.thanks{position:absolute;top:2992px;left:0;width:1200px;text-align:center;font-size:25px;font-weight:300;letter-spacing:.5px}
.thanks b{font-weight:800}
</style>
</head>
<body>
<div class="board-bg"></div>
<div class="board-scene" role="img" aria-label="Faint coastal lighthouse scene fading into the background"></div>

<header class="brand-top">
  <span class="dot"></span>
  <div class="name">SALTMERE<br>ESTATES</div>
  <div class="sub">WINE CO.</div>
</header>

<main class="site">
  <!-- hero -->
  <section class="sec hero">
    <div class="hero-photo" role="img" aria-label="Island lighthouse over a green meadow and water, with two red wine bottles on the right"></div>
    <div class="hero-bottles" role="img" aria-label="Two red wine bottles"></div>
    <nav class="nav">
      <a style="left:190px">Wines</a>
      <a style="left:220px">Wine Club</a>
      <a style="left:264px">Our Story</a>
      <span class="logo">SALTMERE<br>ESTATES</span>
      <a style="left:376px">Visit Us</a>
      <a style="left:407px">News</a>
      <a style="left:434px">Contact Us</a>
      <span class="icons">
        <svg width="7" height="7" viewBox="0 0 10 10"><path d="M1 2h2l1.5 5h4l1-3.5H4" fill="none" stroke="#333"/><circle cx="5" cy="9" r=".8" fill="#333"/><circle cx="8" cy="9" r=".8" fill="#333"/></svg>
        <svg width="7" height="7" viewBox="0 0 10 10"><circle cx="5" cy="3" r="2" fill="none" stroke="#333"/><path d="M1 10c0-3 8-3 8 0" fill="none" stroke="#333"/></svg>
      </span>
    </nav>
    <div class="hero-copy">
      <h1>QUALITY WINE <b>FROM<br>SALTMERE ISLAND</b></h1>
      <p>Lorem ipsum dolor sit amet consectetur. Dictum odio proin aliquam vitae et placerat. Nunc semper leo purus nisl et mauris. Aliquam vel neque gravida lacus morbi tincidunt at ut.</p>
      <div class="btns"><span class="btn-dark">Shop Now →</span><span class="btn-line">Know More About Us →</span></div>
    </div>
    <svg class="hero-edge" viewBox="0 0 655 40" preserveAspectRatio="none"><path d="M0 22 L40 18 L80 24 L130 16 L180 22 L240 15 L300 21 L360 14 L420 20 L480 13 L540 19 L600 12 L655 17 L655 40 L0 40Z" fill="#fff"/></svg>
  </section>

  <!-- about -->
  <section class="sec about">
    <div class="about-photo" role="img" aria-label="Hand holding a bunch of green grapes on the vine"></div>
    <div class="about-bottle" role="img" aria-label="Red wine bottle"></div>
    <div class="about-copy">
      <h3>ABOUT OUR <b>VINEYARD</b></h3>
      <p>Lorem ipsum dolor sit amet consectetur. Lorem ac venenatis imperdiet integer cras egestas amet. Nulla sapien habitasse tempus pulvinar etiam. Commodo consectetur sit blandit scelerisque cursus. Orci massa elementum hendrerit magna.</p>
      <p>Lorem ipsum dolor sit amet consectetur. Lorem ac venenatis imperdiet integer cras egestas amet. Nulla sapien habitasse tempus pulvinar etiam.</p>
      <span class="link-line">Know More About Us →</span>
    </div>
  </section>

  <!-- offer -->
  <section class="sec offer">
    <div class="inner" style="top:50px">
      <h2 class="h2">WHAT WE <b>OFFER</b></h2>
      <p class="lede" style="margin-top:8px">Lorem ipsum dolor sit amet consectetur. Lorem ac venenatis imperdiet integer cras egestas amet. Nulla sapien habitasse tempus pulvinar etiam. Commodo consectetur sit blandit scelerisque cursus. Orci massa elementum hendrerit magna.</p>
    </div>
    <div class="offer-cards">
      <div class="offer-card"><div class="ph" role="img" aria-label="Red wine poured into two glasses" style="background:linear-gradient(160deg,#5a3a30,#8c2a2e 55%,#e9e3df)"></div><span>RED WINE</span></div>
      <div class="offer-card"><div class="ph" role="img" aria-label="White wine glass and bottle with green grapes" style="background:linear-gradient(160deg,#d9b9a3,#e8d6c4 50%,#a9b25a)"></div><span>WHITE WINE</span></div>
      <div class="offer-card"><div class="ph" role="img" aria-label="Rosé wine poured into glasses with berries" style="background:linear-gradient(160deg,#7a7070,#c9c2c0 45%,#d8545c)"></div><span>ROSE WINE</span></div>
    </div>
  </section>

  <!-- winemaking -->
  <section class="sec wine-making">
    <div class="inner" style="top:50px">
      <h2 class="h2">THE <b>WINEMACKING</b></h2>
      <p class="lede" style="margin-top:8px;padding:0 60px">Lorem ipsum dolor sit amet consectetur. Lorem ac venenatis imperdiet integer cras egestas amet. Nulla sapien habitasse tempus pulvinar etiam.</p>
    </div>
    <div class="video" role="img" aria-label="Video still of steel fermentation tanks in a winery">
      <svg class="play" width="28" height="28" viewBox="0 0 28 28"><circle cx="14" cy="14" r="12" fill="none" stroke="#fff" stroke-width="2"/><path d="M11 9l8 5-8 5z" fill="#fff"/></svg>
    </div>
    <div class="stats">
      <div><b>20+</b><span>Years of Experience</span></div>
      <div><b>400k</b><span>Regular Customers</span></div>
      <div><b>250+</b><span>Worldwide Partners</span></div>
      <div><b>300+</b><span>Wine Store</span></div>
    </div>
  </section>

  <!-- shortlist -->
  <section class="sec shortlist">
    <div class="inner" style="top:50px">
      <h2 class="h2">OUR <b>BEST WINE</b> SHORTLIST</h2>
      <p class="lede" style="margin-top:8px;padding:0 60px">Lorem ipsum dolor sit amet consectetur. Lorem ac venenatis imperdiet integer cras egestas amet. Nulla sapien habitasse tempus pulvinar etiam.</p>
    </div>
    <span class="arrow" style="left:86px"><svg width="7" height="5" viewBox="0 0 7 5"><path d="M7 2.5H1M3 .5L1 2.5 3 4.5" fill="none" stroke="#333" stroke-width=".8"/></svg></span>
    <span class="arrow" style="left:552px;background:#1a1a1a"><svg width="7" height="5" viewBox="0 0 7 5"><path d="M0 2.5h6M4 .5l2 2-2 2" fill="none" stroke="#fff" stroke-width=".8"/></svg></span>
    <div class="products">
      <div class="product"><div class="bottle"></div><div class="shadow"></div><div class="stars">★★★★★</div><h4>SE Reserve Harbor<br>Cabernet</h4><div class="price">Price <b>$69.00</b></div></div>
      <div class="product"><div class="bottle"></div><div class="shadow"></div><div class="stars">★★★★★</div><h4>SE Reserve Harbor<br>Cabernet</h4><div class="price">Price <b>$69.00</b></div></div>
      <div class="product"><div class="bottle"></div><div class="shadow"></div><div class="stars">★★★★★</div><h4>SE Reserve Harbor<br>Cabernet</h4><div class="price">Price <b>$69.00</b></div></div>
      <div class="product"><div class="bottle"></div><div class="shadow"></div><div class="stars">★★★★★</div><h4>SE Reserve Harbor<br>Cabernet</h4><div class="price">Price <b>$69.00</b></div></div>
    </div>
  </section>

  <!-- news -->
  <section class="sec news">
    <h3>NEWS &amp; ARTICLES</h3>
    <p class="sub">Stories from our cellar, vineyard rows and harvest days, shared with friends of the estate and island neighbors alike.</p>
    <span class="view-all">View All Articles <svg width="12" height="4" viewBox="0 0 12 4"><path d="M0 2h11M9 .5l2 1.5-2 1.5" fill="none" stroke="#111" stroke-width=".6"/></svg></span>
    <div class="big-photo" role="img" aria-label="Bunches of dark grapes hanging on the vine"></div>
    <div class="article feature">
      <div class="meta">Admin • June 21, 2023</div>
      <h5>Lorem ipsum dolor sit amet. Etiam justo mauris consectetur. Ante massa eu in a laoreet.</h5>
      <p>Lorem ipsum dolor sit amet consectetur. Ante massa eu in a laoreet. Etiam justo mauris sagittis metus. Cras dapibus dignissim pulvinar consectetur massa eu in a laoreet. Etiam justo mauris sagittis metus.</p>
      <div class="author"><i></i><div><b>Mara Quill</b><small>Residential Cleaning</small></div></div>
    </div>
    <div class="news-row">
      <div class="article"><div class="ph" role="img" aria-label="Harvest hands cutting grapes in a vineyard" style="background:linear-gradient(135deg,#3f5a2e,#6a4a3a 50%,#2f3d5e)"></div><div class="meta">Admin • June 21, 2023</div><h5>Lorem ipsum dolor sit amet. Etiam justo mauris consectetur. Ante massa eu in a laoreet.</h5><p>Lorem ipsum dolor sit amet consectetur. Ante massa eu in a laoreet. Etiam justo mauris sagittis metus.</p><div class="author"><i></i><div><b>Mara Quill</b><small>Residential Cleaning</small></div></div></div>
      <div class="article"><div class="ph" role="img" aria-label="Red grape clusters on the vine" style="background:linear-gradient(135deg,#2a2a40,#6a2a3a 50%,#3d5a2a)"></div><div class="meta">Admin • June 21, 2023</div><h5>Lorem ipsum dolor sit amet. Etiam justo mauris consectetur. Ante massa eu in a laoreet.</h5><p>Lorem ipsum dolor sit amet consectetur. Ante massa eu in a laoreet. Etiam justo mauris sagittis metus.</p><div class="author"><i></i><div><b>Teo Barrow</b><small>Residential Cleaning</small></div></div></div>
      <div class="article"><div class="ph" role="img" aria-label="Vineyard rows under a blue sky" style="background:linear-gradient(180deg,#4f78b8,#9db6d8 45%,#4c6a3a 60%,#2f4a28)"></div><div class="meta">Admin • June 21, 2023</div><h5>Lorem ipsum dolor sit amet. Etiam justo mauris consectetur. Ante massa eu in a laoreet.</h5><p>Lorem ipsum dolor sit amet consectetur. Ante massa eu in a laoreet. Etiam justo mauris sagittis metus.</p><div class="author"><i></i><div><b>Lena Rook</b><small>Residential Cleaning</small></div></div></div>
    </div>
  </section>

  <!-- contact -->
  <section class="sec contact">
    <div class="inner" style="top:46px"><h2 class="h2"><b>CONTACT</b> US</h2></div>
    <div class="info">
      <div><svg width="7" height="7" viewBox="0 0 10 10"><path d="M2 1l2 2-1 1.5c.8 1.5 1.5 2.2 3 3L7.5 6l2 2-1.5 1.5C4 9 1 6 .5 1.5z" fill="#fff"/></svg><span>Our Phone<small>+1 555 014 2290</small></span></div>
      <div><svg width="7" height="7" viewBox="0 0 10 10"><rect x=".5" y="2" width="9" height="6" fill="none" stroke="#fff"/><path d="M.5 2l4.5 3.5L9.5 2" fill="none" stroke="#fff"/></svg><span>Email<small>hello@saltmere-estates.test</small></span></div>
      <div style="border:none"><svg width="7" height="7" viewBox="0 0 10 10"><path d="M5 9.5S1.5 6 1.5 4a3.5 3.5 0 017 0C8.5 6 5 9.5 5 9.5z" fill="#fff"/><circle cx="5" cy="4" r="1.2" fill="#222"/></svg><span>Location<small>12 Harbor Lane, Saltmere Island, MA</small></span></div>
    </div>
    <div class="map" role="img" aria-label="Street map of the estate area with location pins"></div>
    <div class="query">HAVE ANY QUERY?</div>
    <div class="form">
      <div class="grid2">
        <div class="field">First Name *<span>Jon Doe</span></div>
        <div class="field">Last Name *<span>example@email.com</span></div>
        <div class="field">Mobile*<span>+1 | 123 456 7890</span></div>
        <div class="field">Email *<span>example@email.com</span></div>
        <div class="field">Please Select *<span>Please Select ⌄</span></div>
        <div class="field">Please Select City *<span>Please Select ⌄</span></div>
        <div class="field full">Message<span>Say Hello....</span></div>
      </div>
      <span class="submit">Submit</span>
    </div>
  </section>

  <!-- footer -->
  <footer class="sec footer">
    <div class="f-brand"><b>SALTMERE ESTATES</b><p>Lorem ipsum dolor sit amet consectetur. Lorem ac venenatis imperdiet integer cras egestas amet. Nulla sapien habitasse tempus pulvinar etiam.</p></div>
    <div class="f-col" style="left:282px"><h6>Links</h6>Our Story<br>Wine Club<br>Visit Us<br>Wines</div>
    <div class="f-col" style="left:352px"><h6>Links</h6>Contact Us<br>Faqs<br>Terms &amp; Conditions<br>Privacy Policy</div>
    <div class="f-col" style="left:446px"><h6>Subscribe Our Newsletter</h6>Lorem ipsum dolor sit amet consectetur.<div class="news-form"><span>Enter your email</span><em>Subscribe</em></div></div>
    <div class="copy">© 2024 Copyrights by Saltmere Estates. All Rights Reserved.</div>
  </footer>
</main>

<p class="thanks"><b>THANK YOU</b> FOR WATCHING</p>
</body>
</html>
```